Modern corporate energy/fuel business need business card design

Business card required for company founder. Korvan Clean Power is a Australian based modern energy/fuel provider. We offer specialised solutions to businesses using fossil fuels through renewable energy solutions.

I would like one side with specific information (name, address etc)

The other side to be bold, professional company name & logo. Striking.

Target Market(s)

B2B. Transport, mining, councils, environmentalist,

Industry/Entity Type

Petroleum

Contact Information for Business Card

Name; Peter Morrow
Position; Director
Email; pmorrow@korvancp.com.au
Address; PO Box 347, Ardmore, QLD, 4820
Website; www.korvancp.com.au

Colors

Designer to choose colors to be used in the design.

Requirements
Must have
• Clean, easy to read, professional & strong theme
Should not have
• too many colours, busy layout,

```html
<!DOCTYPE html>
<html lang="en">
<head>
<meta charset="utf-8">
<title>Korvan Clean Power – Business Card</title>
<link href="https://fonts.googleapis.com/css2?family=Lato:wght@400;700&family=Open+Sans:wght@400;700&display=swap" rel="stylesheet">
<style>
  :root {
    --page: #ffffff;
    --card-bg: #edeef0;
    --card-edge: #dcdddf;
    --band: #ffffff;
    --navy: #235479;
    --orange: #f47b20;
    --ink: #1c1c1c;
    --on-orange: #ffffff;
  }
  html, body {
    margin: 0;
    padding: 0;
    width: 1200px;
    height: 1139px;
    overflow: hidden;
    background: var(--page);
  }
  .sheet { display: block; width: 1200px; height: 1139px; }
  .card-base { fill: var(--card-bg); stroke: var(--card-edge); stroke-width: 1.5; }
  .card-band { fill: var(--band); }
  .chevron-navy { fill: var(--navy); }
  .panel-orange { fill: var(--orange); }
  .brand-mark { fill: var(--orange); }
  .brand-name {
    font-family: "Lato", sans-serif;
    font-weight: 700;
    font-size: 19px;
    fill: var(--navy);
    letter-spacing: 0.5px;
  }
  .contact-text {
    font-family: "Lato", sans-serif;
    font-weight: 400;
    font-size: 15px;
    fill: var(--ink);
  }
  .contact-icon { fill: none; stroke: var(--orange); stroke-width: 1.6; stroke-linejoin: round; stroke-linecap: round; }
  .person-name {
    font-family: "Open Sans", sans-serif;
    font-weight: 700;
    font-size: 17px;
    fill: var(--on-orange);
  }
  .person-role {
    font-family: "Open Sans", sans-serif;
    font-weight: 400;
    font-size: 17px;
    fill: var(--on-orange);
  }
</style>
</head>
<body>
<svg class="sheet" viewBox="0 0 750 712" preserveAspectRatio="none" xmlns="http://www.w3.org/2000/svg">

  <g class="card card-front">
    <rect class="card-base" x="111.5" y="44.5" width="526" height="301"/>
    <polygon class="card-band" points="111,99 479,99 486,283 111,283"/>
    <polygon class="chevron-navy" points="340,115 380,115 432,190 380,266 340,266 392,190"/>
    <polygon class="panel-orange" points="384,115 637,115 637,266 384,266 440,190"/>
    <circle class="brand-mark" cx="160" cy="190" r="24"/>
    <text class="brand-name" x="195" y="185">Korvan</text>
    <text class="brand-name" x="195" y="207">Clean Power</text>
  </g>

  <g class="card card-back">
    <rect class="card-base" x="111.5" y="365.5" width="526" height="299"/>
    <polygon class="card-band" points="111,418 479,418 486,602 111,602"/>
    <polygon class="chevron-navy" points="340,434 380,434 432,510 380,585 340,585 392,510"/>
    <polygon class="panel-orange" points="384,434 637,434 637,585 384,585 440,510"/>

    <g class="contact-list">
      <g class="contact-email">
        <rect class="contact-icon" x="126" y="468" width="20" height="15" rx="1"/>
        <polyline class="contact-icon" points="126,469 136,477 146,469"/>
        <text class="contact-text" x="156" y="481">pmorrow@korvancp.com.au</text>
      </g>
      <g class="contact-address">
        <path class="contact-icon" d="M134,519 C128,511 125,506 125,502 A9,9 0 0 1 143,502 C143,506 140,511 134,519 Z"/>
        <circle class="contact-icon" cx="134" cy="502" r="3.2"/>
        <text class="contact-text" x="156" y="514">PO Box 347, Ardmore, QLD, 4820</text>
      </g>
      <g class="contact-web">
        <circle class="contact-icon" cx="135" cy="542" r="9.5"/>
        <ellipse class="contact-icon" cx="135" cy="542" rx="4" ry="9.5"/>
        <line class="contact-icon" x1="125.5" y1="542" x2="144.5" y2="542"/>
        <line class="contact-icon" x1="127" y1="537" x2="143" y2="537"/>
        <line class="contact-icon" x1="127" y1="547" x2="143" y2="547"/>
        <text class="contact-text" x="156" y="547">www.korvancp.com.au</text>
      </g>
    </g>

    <text class="person-name" x="530" y="504" text-anchor="middle">Peter Morrow</text>
    <text class="person-role" x="522" y="534" text-anchor="middle">Director</text>
  </g>
</svg>
</body>
</html>
```